Fair Wind golf balls - the Lantern Collection

I need to design a box for 12 golf balls.
It is the actual lid and sides that need the creative.
Attached is layout that doesn't pop enough.
Someone needs to make it look more prominent
when displayed on Vendora, etc.
I launched the Song of the Heron golf balls - the Meadow Collection
back in 2010. It turned into a flash fad.
That is my goal here .

Please see attached file. My son says it needs to be more
modern, and compared to the golf balls on Vendora looks far
too dull.
Updates

Reason: My initial 5 day window wasn't enough time. Rookies make mistakes. Thanks Owen

Target Market(s)

Women golfers in US and UK

Requirements
Must have
• Classy

```html
<!DOCTYPE html>
<html lang="en">
<head>
<meta charset="utf-8">
<title>Fair Wind Golf Balls – The Lantern Collection box</title>
<link rel="stylesheet" href="https://fonts.googleapis.com/css2?family=Josefin+Sans:wght@300;700&family=Quattrocento&family=Dancing+Script:wght@500&display=swap">
<style>
  :root {
    --board: #222222;
    --paper: #ffffff;
    --ink: #f4f4f4;
    --portrait-deep: #1e3560;
    --portrait-mid: #5b82c4;
    --portrait-light: #c9d8f2;
    --title-font: "Josefin Sans", sans-serif;
    --quote-font: "Quattrocento", serif;
    --script-font: "Dancing Script", cursive;
  }
  * { box-sizing: border-box; margin: 0; padding: 0; }
  html, body { width: 1200px; height: 719px; overflow: hidden; background: var(--paper); }

  .dieline { position: relative; width: 1200px; height: 719px; background: var(--paper); }
  .panel { position: absolute; background: var(--board); overflow: hidden; color: var(--ink); }

  .glue-flap-left  { left: 0;    top: 147px; width: 133px; height: 425px; }
  .side-left       { left: 134px; top: 147px; width: 162px; height: 425px; }
  .lid-front       { left: 297px; top: 147px; width: 605px; height: 425px; }
  .side-right      { left: 903px; top: 147px; width: 148px; height: 425px; }
  .glue-flap-right { left: 1054px; top: 147px; width: 146px; height: 425px; }
  .flap-top        { left: 297px; top: 0;     width: 605px; height: 146px; }
  .flap-bottom     { left: 297px; top: 573px; width: 605px; height: 146px; }

  .brand-title { font-family: var(--title-font); font-weight: 700; line-height: 1; white-space: nowrap; }
  .brand-sub { font-family: var(--title-font); font-weight: 300; line-height: 1; letter-spacing: 0.32em; white-space: nowrap; }
  .collection { font-family: var(--script-font); font-weight: 500; line-height: 1; white-space: nowrap; }

  .portrait-strip {
    position: absolute;
    border-radius: 40% 40% 8px 8px / 60% 60% 8px 8px;
    background:
      radial-gradient(ellipse at 50% 40%, var(--portrait-light) 0%, transparent 55%),
      linear-gradient(90deg, var(--portrait-deep), var(--portrait-mid) 25%, var(--portrait-deep) 45%, var(--portrait-mid) 70%, var(--portrait-deep));
    box-shadow: 0 0 14px 4px rgba(180, 200, 240, 0.25);
  }

  /* Front lid */
  .lid-front .tagline {
    position: absolute; top: 28px; left: 0; width: 100%;
    text-align: center; font-family: var(--quote-font); font-size: 19px; line-height: 31px;
  }
  .lid-front .brand-title { position: absolute; top: 120px; width: 100%; text-align: center; font-size: 74px; }
  .lid-front .brand-sub { position: absolute; top: 198px; width: 100%; text-align: center; font-size: 27px; padding-left: 0.32em; }
  .lid-front .portrait-strip { left: 55px; top: 240px; width: 515px; height: 120px; }
  .lid-front .collection { position: absolute; top: 372px; width: 100%; text-align: center; font-size: 34px; }

  /* Top and bottom flaps */
  .flap-lockup { position: absolute; inset: 0; }
  .flap-top .flap-lockup { transform: rotate(180deg); }
  .flap-lockup .brand-title { position: absolute; left: 50px; top: 40px; font-size: 46px; }
  .flap-lockup .brand-sub { position: absolute; left: 56px; top: 92px; font-size: 18px; }
  .flap-lockup .portrait-strip { left: 322px; top: 40px; width: 255px; height: 60px; }
  .flap-lockup .collection { position: absolute; left: 322px; top: 108px; width: 255px; text-align: center; font-size: 20px; }

  /* Side panels */
  .side-lockup {
    position: absolute; left: 50%; top: 50%; width: 400px; height: 150px;
    display: flex; flex-direction: column; align-items: center;
  }
  .side-left .side-lockup  { transform: translate(-50%, -50%) rotate(90deg); }
  .side-right .side-lockup { transform: translate(-50%, -50%) rotate(-90deg); }
  .side-lockup .brand-line { margin-top: 10px; display: flex; align-items: baseline; gap: 16px; }
  .side-lockup .brand-title { font-size: 30px; }
  .side-lockup .brand-sub { font-size: 22px; }
  .side-lockup .portrait-strip { position: relative; margin-top: 14px; width: 245px; height: 58px; }
  .side-lockup .collection { margin-top: 8px; font-size: 20px; }
</style>
</head>
<body>
<main class="dieline">

  <section class="panel flap-top">
    <div class="flap-lockup">
      <div class="brand-title">FAIR WIND</div>
      <div class="brand-sub">GOLF BALLS</div>
      <div class="portrait-strip" role="img" aria-label="Row of five blue-toned celebrity portrait photos"></div>
      <div class="collection">The Lantern Collection</div>
    </div>
  </section>

  <section class="panel glue-flap-left"></section>

  <section class="panel side-left">
    <div class="side-lockup">
      <div class="brand-line">
        <span class="brand-title">FAIR WIND</span>
        <span class="brand-sub">GOLF BALLS</span>
      </div>
      <div class="portrait-strip" role="img" aria-label="Row of five blue-toned celebrity portrait photos"></div>
      <div class="collection">The Lantern Collection</div>
    </div>
  </section>

  <section class="panel lid-front">
    <p class="tagline">“Cheating is a choice not a mistake,”<br>so choose…</p>
    <h1 class="brand-title">FAIR WIND</h1>
    <div class="brand-sub">GOLF BALLS</div>
    <div class="portrait-strip" role="img" aria-label="Row of five blue-toned celebrity portrait photos"></div>
    <div class="collection">The Lantern Collection</div>
  </section>

  <section class="panel side-right">
    <div class="side-lockup">
      <div class="brand-line">
        <span class="brand-title">FAIR WIND</span>
        <span class="brand-sub">GOLF BALLS</span>
      </div>
      <div class="portrait-strip" role="img" aria-label="Row of five blue-toned celebrity portrait photos"></div>
      <div class="collection">The Lantern Collection</div>
    </div>
  </section>

  <section class="panel glue-flap-right"></section>

  <section class="panel flap-bottom">
    <div class="flap-lockup">
      <div class="brand-title">FAIR WIND</div>
      <div class="brand-sub">GOLF BALLS</div>
      <div class="portrait-strip" role="img" aria-label="Row of five blue-toned celebrity portrait photos"></div>
      <div class="collection">The Lantern Collection</div>
    </div>
  </section>

</main>
</body>
</html>
```